Business Card Design for Oncology Consulting Company

We need a business card design using a logo that has already been created.

Company name is: ORBVA - Guild for Lumora Mapping, Welfare and Outreach

We would also like to include the following pieces of information on the business card:
Name
Title
US Address (street, city, state, zip, country)
Email address
Website address

Target Market(s)

The target customers are physicians (oncologists, pathologists) in Greece, Iran, US, etc who would refer patients to our company for a second medical opinion/genetic counseling for cancer.

Industry/Entity Type

Business

Colors

Designer to choose colors to be used in the design.

Requirements
Must have
• Must contain logo in attached file and elements described above.

```html
<!DOCTYPE html>
<html lang="en">
<head>
<meta charset="utf-8">
<title>ORBVA Business Card</title>
<link href="https://fonts.googleapis.com/css2?family=Ubuntu:wght@400;500;700&display=swap" rel="stylesheet">
<style>
  :root {
    --backdrop: #3a3a3a;
    --card-white: #ffffff;
    --brand-blue: #1467b1;
    --brand-blue-light: #4d8fcc;
    --tagline-grey: #6b7f93;
    --text-white: #ffffff;
  }
  html, body {
    margin: 0;
    padding: 0;
    width: 1006px;
    height: 1200px;
    overflow: hidden;
    background: var(--backdrop);
    font-family: "Ubuntu", sans-serif;
  }
  .canvas {
    position: relative;
    width: 1006px;
    height: 1200px;
  }
  .card {
    position: absolute;
    left: 88px;
    width: 838px;
    height: 491px;
    overflow: hidden;
  }
  .card-front { top: 82px; background: var(--card-white); }
  .card-back { top: 627px; background: var(--brand-blue); }

  /* Brand lockup: name followed by a ruled tagline block */
  .brand-lockup {
    position: absolute;
    display: flex;
    align-items: flex-end;
  }
  .brand-name {
    margin: 0;
    font-weight: 700;
    letter-spacing: -1px;
    line-height: 0.8;
    white-space: nowrap;
  }
  .brand-detail {
    display: flex;
    flex-direction: column;
  }
  .brand-rule {
    height: 1px;
    width: 100%;
  }
  .brand-tagline {
    margin: 0;
    font-weight: 500;
    text-transform: uppercase;
    line-height: 1;
    white-space: nowrap;
  }

  .card-front .brand-lockup { left: 52px; top: 64px; }
  .card-front .brand-name { font-size: 58px; color: var(--brand-blue); }
  .card-front .brand-detail { margin-left: 14px; width: 206px; margin-bottom: -9px; }
  .card-front .brand-rule { background: var(--tagline-grey); margin-bottom: 2px; }
  .card-front .brand-tagline { font-size: 6.5px; color: var(--tagline-grey); }

  .holder {
    position: absolute;
    right: 51px;
    top: 56px;
    text-align: right;
    color: var(--brand-blue);
  }
  .holder-name { margin: 0; font-size: 39px; font-weight: 700; line-height: 1.05; }
  .holder-title { margin: 0; font-size: 22px; font-weight: 700; line-height: 1.1; }

  .contact, .address {
    position: absolute;
    margin: 0;
    font-style: normal;
    font-size: 24px;
    line-height: 31px;
    color: var(--brand-blue);
  }
  .contact { left: 52px; top: 305px; }
  .address { right: 51px; top: 287px; text-align: right; }

  .web-band {
    position: absolute;
    left: 0;
    top: 402px;
    width: 100%;
    height: 57px;
    background: var(--brand-blue);
  }
  .web-address {
    position: absolute;
    left: 52px;
    top: 14px;
    margin: 0;
    font-size: 23px;
    font-weight: 700;
    color: var(--text-white);
  }
  .band-texture {
    position: absolute;
    right: 0;
    top: 0;
    width: 318px;
    height: 57px;
    background: linear-gradient(90deg, var(--brand-blue), var(--brand-blue-light));
  }

  .card-back .brand-lockup { left: 100px; top: 213px; }
  .card-back .brand-name { font-size: 88px; color: var(--text-white); }
  .card-back .brand-detail { margin-left: 24px; width: 328px; margin-bottom: -12px; }
  .card-back .brand-rule { height: 2px; background: var(--text-white); margin-bottom: 4px; }
  .card-back .brand-tagline { font-size: 10px; color: var(--text-white); }
</style>
</head>
<body>
<div class="canvas">
  <section class="card card-front">
    <div class="brand-lockup">
      <h1 class="brand-name">ORBVA</h1>
      <div class="brand-detail">
        <div class="brand-rule"></div>
        <p class="brand-tagline">Guild for Lumora Mapping, Welfare and Outreach</p>
      </div>
    </div>

    <div class="holder">
      <p class="holder-name">Mara Velden</p>
      <p class="holder-title">CEO</p>
    </div>

    <p class="contact">555-314-2096<br>mv@orbvanet.com</p>
    <address class="address">4170 Larkspur Lane<br>Belmont (Quebec) H3K 2P8<br>USA</address>

    <div class="web-band">
      <p class="web-address">www.orbva.com</p>
      <div class="band-texture" role="img" aria-label="Decorative pattern of scattered light blue dots"></div>
    </div>
  </section>

  <section class="card card-back">
    <div class="brand-lockup">
      <h2 class="brand-name">ORBVA</h2>
      <div class="brand-detail">
        <div class="brand-rule"></div>
        <p class="brand-tagline">Guild for Lumora Mapping, Welfare and Outreach</p>
      </div>
    </div>
  </section>
</div>
</body>
</html>
```